Harborline Network Advisors (HNA) Business Card

Front Side, add Company Logo
1.) Harborline Network Advisors
Director of Operations
Delgado, Marco T
(323) 555 0148
782 n Alder Ave Suite 300 PMB2093
Los Angeles, CA 90013
Marco@HarborlineNA.example
www.HarborlineNA.example
2.) Veteran-Owned Business (with Small EGA)

Back Side
- Pictures are ideas of what you can add. The description is what HNA does.
1.) Business Partners:
- Corvalis Business
- KX&L Business
- Tellmora Business
2.) What we do
- Broker of Internet service (partners above)
- Project Management/ Contract Management
- Government Contracts

```html
<!DOCTYPE html>
<html lang="en">
<head>
<meta charset="utf-8">
<title>Harborline Network Advisors – Business Card</title>
<link href="https://fonts.googleapis.com/css2?family=Marcellus&family=Philosopher:wght@400;700&display=swap" rel="stylesheet">
<style>
  :root {
    --ink: #1f1d1e;
    --gold: #f0b41c;
    --paper: #f4f4f4;
    --text: #2b2b2b;
    --stage: #e6e3df;
  }
  * { box-sizing: border-box; margin: 0; padding: 0; }
  html, body { width: 1200px; height: 900px; overflow: hidden; }
  body {
    background: var(--stage);
    position: relative;
    font-family: "Marcellus", "Georgia", serif;
    color: var(--text);
  }
  .card {
    position: absolute;
    width: 700px;
    height: 400px;
    background: var(--paper);
    box-shadow: 0 8px 24px rgba(0,0,0,.22);
    overflow: hidden;
  }
  .card--back { left: 80px; top: 40px; }
  .card--front { left: 420px; top: 460px; }
  .card__shapes { position: absolute; inset: 0; }

  /* company mark */
  .brand {
    position: absolute;
    display: flex;
    flex-direction: column;
    align-items: center;
    text-align: center;
    color: var(--gold);
    font-size: 21px;
    letter-spacing: 2px;
    line-height: 1.25;
    text-transform: uppercase;
  }
  .brand__dot {
    width: 42px; height: 42px;
    border-radius: 50%;
    background: var(--gold);
    margin-bottom: 14px;
  }
  .card--back .brand { left: 510px; top: 50px; width: 200px; }
  .card--front .brand { left: 10px; top: 120px; width: 260px; }

  /* back side */
  .partners__label {
    position: absolute; left: 40px; top: 80px;
    font-family: "Philosopher", sans-serif;
    font-weight: 700; font-size: 20px; color: #444;
  }
  .partners__list {
    position: absolute; left: 22px; top: 130px;
    display: flex; gap: 10px;
  }
  .partner {
    background: #fff;
    padding: 9px 10px;
    font-size: 14px;
    color: var(--ink);
    white-space: nowrap;
    display: flex; align-items: center; gap: 6px;
  }
  .partner__sq { width: 11px; height: 11px; background: var(--ink); }
  .services { position: absolute; left: 40px; top: 218px; }
  .services__title {
    font-family: "Philosopher", sans-serif;
    font-weight: 700; font-size: 22px; color: #111;
    margin-bottom: 6px;
  }
  .services__list { list-style: none; font-size: 20px; color: #333; line-height: 1.45; }
  .services__list li { display: flex; align-items: center; gap: 10px; }
  .services__list li::before {
    content: ""; width: 10px; height: 10px; border-radius: 50%;
    background: var(--gold); flex: none;
  }

  /* front side */
  .person {
    position: absolute; right: 30px; top: 116px; text-align: right;
  }
  .person__name {
    font-family: "Philosopher", sans-serif;
    font-weight: 700; font-size: 30px; color: var(--gold); line-height: 1.1;
  }
  .person__role { font-size: 21px; color: #fff; }
  .contact {
    position: absolute; right: 24px; top: 222px;
    list-style: none; text-align: right;
    font-size: 17px; line-height: 1.55; color: var(--text);
  }
  .contact li { display: flex; justify-content: flex-end; align-items: center; gap: 8px; }
  .contact svg { width: 16px; height: 16px; fill: var(--ink); flex: none; }
  .address {
    position: absolute; right: 24px; top: 334px;
    font-size: 17px; line-height: 1.45; text-align: right; color: var(--text);
  }
  .address__line { display: flex; justify-content: flex-end; align-items: center; gap: 8px; white-space: nowrap; }
  .address svg { width: 16px; height: 16px; fill: var(--ink); flex: none; }
  .address__city { padding-right: 24px; }
</style>
</head>
<body>

<section class="card card--back" aria-label="Business card back">
  <svg class="card__shapes" viewBox="0 0 700 400" aria-hidden="true">
    <polygon points="0,120 468,120 504,180 0,180" fill="var(--ink)"/>
    <line x1="0" y1="114" x2="464" y2="114" stroke="var(--gold)" stroke-width="4"/>
    <line x1="0" y1="186" x2="508" y2="186" stroke="var(--gold)" stroke-width="4"/>
    <polygon points="416,0 700,0 700,400 656,400" fill="var(--ink)"/>
    <line x1="400" y1="0" x2="640" y2="400" stroke="var(--gold)" stroke-width="6"/>
  </svg>

  <div class="partners__label">Business Partners :</div>
  <div class="partners__list">
    <div class="partner"><span class="partner__sq"></span>KX&amp;L Business</div>
    <div class="partner">Corvalis Business</div>
    <div class="partner">Tellmora Business</div>
  </div>

  <div class="services">
    <div class="services__title">What we do -</div>
    <ul class="services__list">
      <li>Broker of Internet service (partners above)</li>
      <li>Project Management/ Contract Management</li>
      <li>Government Contracts</li>
    </ul>
  </div>

  <div class="brand">
    <span class="brand__dot"></span>
    Harborline<br>Network<br>Advisors
  </div>
</section>

<section class="card card--front" aria-label="Business card front">
  <svg class="card__shapes" viewBox="0 0 700 400" aria-hidden="true">
    <polygon points="0,0 220,0 330,400 0,400" fill="var(--ink)"/>
    <line x1="234" y1="0" x2="344" y2="400" stroke="var(--gold)" stroke-width="6"/>
    <polygon points="278,110 700,110 700,190 300,190" fill="var(--ink)"/>
    <line x1="275" y1="104" x2="700" y2="104" stroke="var(--gold)" stroke-width="4"/>
    <line x1="302" y1="196" x2="700" y2="196" stroke="var(--gold)" stroke-width="4"/>
    <line x1="400" y1="322" x2="676" y2="322" stroke="var(--gold)" stroke-width="2"/>
  </svg>

  <div class="brand">
    <span class="brand__dot"></span>
    Harborline<br>Network<br>Advisors
  </div>

  <div class="person">
    <div class="person__name">Delgado, Marco T</div>
    <div class="person__role">Director of Operations</div>
  </div>

  <ul class="contact">
    <li>(323) 555 0148
      <svg viewBox="0 0 24 24" aria-label="Phone"><path d="M6.6 10.8a15 15 0 0 0 6.6 6.6l2.2-2.2c.3-.3.7-.4 1-.2 1.1.4 2.3.6 3.6.6.6 0 1 .4 1 1V20c0 .6-.4 1-1 1A17 17 0 0 1 3 4c0-.6.4-1 1-1h3.5c.6 0 1 .4 1 1 0 1.3.2 2.5.6 3.6.1.3 0 .7-.2 1z"/></svg>
    </li>
    <li>Marco@HarborlineNA.example
      <svg viewBox="0 0 24 24" aria-label="Email"><path d="M2 5h20v14H2zM4 7v.5l8 5 8-5V7l-8 5z"/></svg>
    </li>
    <li>www.HarborlineNA.example
      <svg viewBox="0 0 24 24" aria-label="Website"><path d="M12 2a10 10 0 1 0 0 20 10 10 0 0 0 0-20zm0 2c1 1.2 1.8 3 2.1 5H9.9C10.2 7 11 5.2 12 4zM4.3 11h3.6a17 17 0 0 0 0 2H4.3a8 8 0 0 1 0-2zm5.6 0h4.2a15 15 0 0 1 0 2H9.9a15 15 0 0 1 0-2zm6.2 0h3.6a8 8 0 0 1 0 2h-3.6a17 17 0 0 0 0-2zM12 20c-1-1.2-1.8-3-2.1-5h4.2c-.3 2-1.1 3.8-2.1 5z"/></svg>
    </li>
  </ul>

  <div class="address">
    <div class="address__line">782 n Alder Ave Suite 300 PMB2093
      <svg viewBox="0 0 24 24" aria-label="Location"><path d="M12 2a7 7 0 0 0-7 7c0 5 7 13 7 13s7-8 7-13a7 7 0 0 0-7-7zm0 9.5A2.5 2.5 0 1 1 12 6.5a2.5 2.5 0 0 1 0 5z"/></svg>
    </div>
    <div class="address__city">Los Angeles, CA 90013</div>
  </div>
</section>

</body>
</html>
```